Harborview House and Shelter for Servicemembers needs an invitation for our Gala

The size is 15 x 7 but will need to fold to 5.25 x 7.25 (an A7 envelope) The invitation can appear vertical or horizontally. This is a 4 color, 2 sided invitation.
The design inspiration should come from the event logo. The logo can appear long or can be stacked.
The text needed and the logo for the event are attached.
The Harborview House and Shelter for Servicemembers, is hosting it's 14th Annual Stand Together Always Gala on November 2nd at the Quayside Exchange Pavilion. We are looking for a new design concept for our invitation and program book materials using an existing logo.
The concept can use images, however if the designer chooses to use an image, they must incorporate all military branches and both men and women. The final design should communicate elegance and be reflective of the organization and event logo. We will take into consideration a four, two or one color design. Lastly, the HHSS and event logos can appear next to each other or side by side.
Our mission: The Harborview House for Unhoused Servicemembers was founded in 1989 and is a private not-for-profit organization. The Center is one of the nation’s largest private resources for Veterans of every era who may be facing challenges and are at-risk of homelessness. Our experienced professionals provide the tools and direct Veterans to resources that enable successful independent living and meaningful employment.
Here's a link to our website for reference:
hhss-shelter.org

```html
<!DOCTYPE html>
<html lang="en">
<head>
<meta charset="utf-8">
<title>Stand Together Always Gala – Invitation</title>
<link href="https://fonts.googleapis.com/css2?family=Oswald:wght@500;700&family=Cinzel:wght@400&display=swap" rel="stylesheet">
<style>
  :root {
    --page: #eceef0;
    --paper-top: #6dbde9;
    --paper-mid: #c4e2f5;
    --paper-low: #d6ebf8;
    --ink: #111418;
    --navy: #24386b;
  }
  * { box-sizing: border-box; margin: 0; padding: 0; }
  html, body { width: 1200px; height: 1200px; overflow: hidden; background: var(--page); }
  .invitation {
    position: absolute; left: 220px; top: 50px; width: 760px; height: 1100px;
    background: linear-gradient(180deg, var(--paper-top) 0, var(--paper-mid) 220px, var(--paper-low) 100%);
    box-shadow: 0 6px 24px rgba(0,0,0,0.18);
    overflow: hidden;
    font-family: 'Oswald', 'Arial Narrow', sans-serif;
    color: var(--ink);
    text-align: center;
  }
  .content { position: relative; padding-top: 56px; }
  .invite-line { font-size: 26px; font-weight: 700; letter-spacing: 0.5px; }
  .event-logo {
    display: flex; align-items: center; justify-content: center; gap: 16px;
    margin-top: 26px;
  }
  .event-logo .mark { width: 28px; height: 28px; border-radius: 50%; background: var(--navy); flex: none; }
  .event-logo .name {
    font-family: 'Cinzel', serif; font-weight: 400; color: var(--navy);
    font-size: 34px; line-height: 1.15;
  }
  .date { font-size: 30px; font-weight: 700; margin-top: 48px; }
  .venue { font-size: 30px; font-weight: 700; margin-top: 4px; }
  .address { font-size: 22px; font-weight: 700; margin-top: 2px; }
  .program { margin-top: 80px; }
  .schedule { font-size: 19px; font-weight: 700; line-height: 1.3; }
  .roles { margin-top: 22px; font-size: 14px; font-weight: 700; line-height: 1.3; }
  .roles .name { font-size: 18px; }
  .roles .tba { font-size: 17px; }
  .roles dt { margin-top: 8px; }
  .closing-rule { width: 620px; margin: 20px auto 0; border-top: 2px solid var(--ink); }
  .notes { margin-top: 12px; font-size: 14px; font-weight: 700; line-height: 1.45; }
</style>
</head>
<body>
<main class="invitation">
  <div class="content">
    <p class="invite-line">You are cordially invited to the</p>
    <div class="event-logo">
      <span class="mark" aria-hidden="true"></span>
      <h1 class="name">14th Annual<br>Stand Together Always Gala</h1>
    </div>
    <p class="date">Wednesday, November 2, 2016</p>
    <p class="venue">Quayside Exchange Pavilion</p>
    <p class="address">48 Harbor Point Boulevard, Bayport, Massachusetts</p>

    <section class="program">
      <p class="schedule">5:30 PM - Reception and Silent Auction<br>7:00 PM - Dinner, Live Auction, and Awards Program</p>
      <dl class="roles">
        <dt>Master of Ceremonies</dt>
        <dd class="name">Daniel Rourke</dd>
        <dd>Evening Anchor, Coastline News Network</dd>
        <dt>Keynote Speaker</dt>
        <dd class="tba">tba</dd>
        <dt>Our National Anthem</dt>
        <dd class="tba">tba</dd>
        <dt>Battlefield Citation</dt>
        <dd class="tba">tba</dd>
        <dt>Thomas E. Hale, Distinguished Service for Veterans Award</dt>
        <dd class="tba">tba</dd>
        <dt>Corporate Partner</dt>
        <dd class="tba">tba</dd>
        <dd class="tba">tba</dd>
        <dt class="name">R. Michael Dunmore</dt>
        <dd>President and Chief Executive Officer</dd>
      </dl>
      <div class="closing-rule"></div>
      <p class="notes">Black Tie Optional - Reply Card Enclosed<br>
        For more information about the event, please contact Claire Whitfield at 555-014-2280 or email c.whitfield@hhss-shelter.org<br>
        Self-Parking at the Quayside Parking Garage is $23. Valet parking for the event is $33</p>
    </section>
  </div>
</main>
</body>
</html>
```